NEED POWERPOINT TEMPLATE for Velora Systems Group is working in Future Technologies

Velora Systems Group (VLSG) works in the area of building Products and Services in the area of Artificial Intelligence and Quantum Computing. We have built Center of Excellence in AI and Quantum Technology Development. Attached are the logo files

Looking for Powerpoint template to use for client presentations.

Target Market(s)

Deep Tech and Future Technologies, Artificial Intelligence market

Industry/Entity Type

Information Technology

Requirements
Must have
• Contemporary and Modern Look
Nice to have
• Will leave it to Designer choice
Should not have
• Nothing at this point

```html
<!DOCTYPE html>
<html lang="en">
<head>
<meta charset="utf-8">
<title>Velora Systems Group – Presentation Template</title>
<link href="https://fonts.googleapis.com/css2?family=Poppins:wght@300;400;500;600;700;800&display=swap" rel="stylesheet">
<style>
:root{
  --backdrop:#77787d;
  --indigo:#4a33c4;
  --violet:#5a3fd8;
  --deep:#2e2384;
  --cyan:#14c3ea;
  --sky:#12a8ee;
  --ink:#2a2a33;
  --text:#5a5a63;
  --panel:#e3e3e8;
  --white:#ffffff;
}
*{box-sizing:border-box;margin:0;padding:0}
html,body{width:1052px;height:1200px;overflow:hidden}
body{background:var(--backdrop);font-family:"Poppins",sans-serif;color:var(--ink);position:relative}
.board{position:absolute;left:62px;top:54px;display:grid;grid-template-columns:repeat(3,305px);grid-auto-rows:171px;column-gap:12px;row-gap:13px}
.slide{position:relative;background:var(--white);overflow:hidden;box-shadow:2px 3px 5px rgba(0,0,0,.35)}
.abs{position:absolute}
.p{font-size:3.2px;line-height:4.3px;color:var(--text);text-align:justify}
.kicker{color:var(--cyan);font-weight:500;text-transform:uppercase;line-height:1}
.head{color:var(--violet);font-weight:800;text-transform:uppercase;line-height:1}
.mark{position:absolute;right:7px;bottom:5px;display:flex;align-items:center;gap:2px;font-size:3.2px;font-weight:700;color:var(--ink)}
.mark i{display:flex;align-items:center;justify-content:center;width:9px;height:9px;border-radius:50%;border:1px solid var(--sky);font-style:normal;font-size:3px;color:var(--violet)}
.baseline{position:absolute;left:0;right:0;bottom:6px;height:.5px;background:linear-gradient(90deg,var(--cyan),var(--violet) 60%,transparent)}
.art{position:absolute}
.tri{display:inline-block;width:0;height:0;border-left:3.5px solid var(--sky);border-top:2px solid transparent;border-bottom:2px solid transparent;margin-right:4px;vertical-align:top;margin-top:1px;flex:none}
.bullet{display:flex;font-size:3px;line-height:4px;color:var(--text)}
.lbl{font-size:5px;font-weight:600;color:var(--violet)}
.legend{display:flex;gap:3px}
.legend b{flex:none;width:4px;height:4px;border-radius:50%;margin-top:1px}
.legend .lbl{font-size:4.4px}
.option{position:absolute;width:34px}
.option b{display:block;font-size:3.5px;font-weight:700;color:var(--cyan)}
</style>
</head>
<body>
<main class="board">

<!-- 1 cover -->
<section class="slide">
  <div class="abs" style="left:12px;top:22px;display:flex;align-items:center;gap:4px">
    <span style="width:10px;height:10px;border-radius:50%;background:var(--violet)"></span>
    <span style="font-size:8.5px;font-weight:700;color:var(--ink)">VELORA SYSTEMS GROUP</span>
  </div>
  <div class="abs kicker" style="left:13px;top:89px;font-size:7.5px;font-weight:400">Presentation</div>
  <div class="abs" style="left:12px;top:100px;font-size:19px;font-weight:800;color:var(--ink)">BUSINESS</div>
  <div class="abs" style="left:12px;top:122px;font-size:17.5px;font-weight:800;color:var(--violet)">MARKETING</div>
  <div class="abs" style="left:13px;top:154px;font-size:6px;color:var(--violet)">www.velorasystemsgroup.com</div>
  <div class="art" role="img" aria-label="Cover artwork: blue glowing AI chip with circuit network, robotic figure and curved orbit bands" style="left:135px;top:0;width:170px;height:171px;background:radial-gradient(circle at 65% 45%,#6fa8ff,#2a4fd0 45%,#251a8a 90%)"></div>
</section>

<!-- 2 contents -->
<section class="slide">
  <div class="art" role="img" aria-label="Isometric illustration of a robot on a platform with servers, cloud and brain" style="left:22px;top:22px;width:140px;height:125px;border-radius:8px;background:radial-gradient(circle,#dcd8fb,#f3f7ff 70%,#fff)"></div>
  <div class="abs" style="left:169px;top:22px;font-size:14px;font-weight:600;color:var(--violet)">Contents</div>
  <div class="abs" style="left:169px;top:40px;width:68px;height:1px;background:var(--violet)"></div>
  <div class="abs" style="left:169px;top:50px;width:112px;display:flex;flex-direction:column;gap:9px">
    <div style="display:flex;gap:4px"><span style="font-size:6px;color:var(--cyan)">1.</span><div><div style="font-size:5.5px;font-weight:500">Lorem ipsum</div><div class="p" style="font-size:3px;line-height:4px">Lorem ipsum dolor sit amet, consectetuer adipiscing elit, sed diam nonummy nibh euismod tincid</div></div></div>
    <div style="display:flex;gap:4px"><span style="font-size:6px;color:var(--cyan)">2.</span><div><div style="font-size:5.5px;font-weight:500">Lorem ipsum</div><div class="p" style="font-size:3px;line-height:4px">Lorem ipsum dolor sit amet, consectetuer adipiscing elit, sed diam nonummy nibh euismod tincid</div></div></div>
    <div style="display:flex;gap:4px"><span style="font-size:6px;color:var(--cyan)">3.</span><div><div style="font-size:5.5px;font-weight:500">Lorem ipsum</div><div class="p" style="font-size:3px;line-height:4px">Lorem ipsum dolor sit amet, consectetuer adipiscing elit, sed diam nonummy nibh euismod tincid</div></div></div>
    <div style="display:flex;gap:4px"><span style="font-size:6px;color:var(--cyan)">4.</span><div><div style="font-size:5.5px;font-weight:500">Lorem ipsum</div><div class="p" style="font-size:3px;line-height:4px">Lorem ipsum dolor sit amet, consectetuer adipiscing elit, sed diam nonummy nibh euismod tincid</div></div></div>
  </div>
  <div class="baseline"></div><div class="mark">VELORA SYSTEMS GROUP <i>02</i></div>
</section>

<!-- 3 data our company -->
<section class="slide">
  <div class="abs" style="left:20px;top:15px;width:145px;height:136px;background:var(--panel)"></div>
  <div class="abs kicker" style="left:31px;top:28px;font-size:11px">Data our</div>
  <div class="abs head" style="left:31px;top:42px;font-size:11.5px">Company</div>
  <div class="abs p" style="left:31px;top:62px;width:115px">Lorem ipsum dolor sit amet, consectetuer adipiscing elit, sed diam nonummy nibh euismod tincidunt ut laoreet dolore magna aliquam erat volutpat. Ut wisi enim ad minim veniam, quis nostrud exerci tation ullamcorper suscipit lobortis nisl ut aliquip ex ea commodo consequat. Duis autem vel eum iriure dolor in hendrerit in vulputate velit esse molestie consequat, vel illum dolore eu feugiat nulla facilisis at vero eros et accumsan et iusto odio dignissim qui blandit praesent luptatum zzril delenit.</div>
  <div class="abs p" style="left:31px;top:121px;width:115px">Lorem ipsum dolor sit amet, cons ectetuer adipiscing elit, sed diam nonummy nibh euismod tincidunt ut laoreet dolore magna aliquam erat volutpat. Ut wisi enim ad minim veniam, quis nostrud</div>
  <div class="abs" style="left:153px;top:24px;display:flex;flex-direction:column;gap:20px">
    <div style="display:flex;gap:6px"><span style="flex:none;width:21px;height:21px;border-radius:50%;background:var(--violet);border:2px solid #cfcaf5"></span><div style="width:100px"><div class="lbl" style="color:var(--cyan);font-size:5.8px">Lorem ipsum</div><div class="p">ipsum dolor sit amet, cons ectetuer adipiscing elit, sed diam nonummy nibh euismod tincidunt ut laoreet dolore magna aliquam erat volutpat. Ut wisi enim ad minim veniam, quis nostrud</div></div></div>
    <div style="display:flex;gap:6px"><span style="flex:none;width:21px;height:21px;border-radius:50%;background:var(--violet);border:2px solid #cfcaf5"></span><div style="width:100px"><div class="lbl" style="color:var(--cyan);font-size:5.8px">Lorem ipsum</div><div class="p">ipsum dolor sit amet, cons ectetuer adipiscing elit, sed diam nonummy nibh euismod tincidunt ut laoreet dolore magna aliquam erat volutpat. Ut wisi enim ad minim veniam, quis nostrud</div></div></div>
    <div style="display:flex;gap:6px"><span style="flex:none;width:21px;height:21px;border-radius:50%;background:var(--violet);border:2px solid #cfcaf5"></span><div style="width:100px"><div class="lbl" style="color:var(--cyan);font-size:5.8px">Lorem ipsum</div><div class="p">ipsum dolor sit amet, cons ectetuer adipiscing elit, sed diam nonummy nibh euismod tincidunt ut laoreet dolore magna aliquam erat volutpat. Ut wisi enim ad minim veniam, quis nostrud</div></div></div>
  </div>
  <div class="baseline"></div><div class="mark">VELORA SYSTEMS GROUP <i>03</i></div>
</section>

<!-- 4 active intelligence -->
<section class="slide">
  <div class="abs" style="left:20px;top:13px;width:83px;height:2px;background:var(--cyan)"></div>
  <div class="art" role="img" aria-label="Photo of a white humanoid robot touching a holographic interface" style="left:0;top:18px;width:177px;height:127px;background:linear-gradient(120deg,#e9eef5,#b9c9dd 55%,#8ea3c2)"></div>
  <div class="abs" style="left:182px;top:18px;width:1px;height:133px;background:var(--violet)"></div>
  <div class="abs" style="left:100px;top:150px;width:83px;height:1.5px;background:var(--violet)"></div>
  <div class="abs kicker" style="left:190px;top:20px;font-size:9.5px">Active</div>
  <div class="abs head" style="left:190px;top:32px;font-size:9.5px">Intelligence</div>
  <div class="abs p" style="left:190px;top:46px;width:100px">Lorem ipsum dolor sit amet, consectetuer adipiscing elit, sed diam nonummy nibh euismod tincidunt ut laoreet dolore magna aliquam erat volutpat. Ut wisi enim ad minim veniam, quis nostrud exerci tation ullamcorper suscipit lobortis nisl ut aliquip ex ea commodo consequat. Duis autem vel eum iriure dolor in hendrerit in vulputate velit esse</div>
  <div class="abs p" style="left:190px;top:81px;width:100px">Lorem ipsum dolor sit amet, consectetuer adipiscing elit, sed diam nonummy nibh euismod tincidunt ut laoreet dolore magna aliquam erat volutpat. Ut wisi enim ad minim veniam, quis nostrud exerci tation ullamcorper suscipit lobortis nisl ut aliquip ex ea commodo consequat. Duis autem vel eum iriure dolor in hendrerit in vulputate velit esse</div>
  <div class="abs bullet" style="left:190px;top:116px;width:100px"><span class="tri"></span><span>Lorem ipsum dolor sit amet, consectetuer adipiscing elit, sed diam nonummy nibh euismod tincidunt ut laoreet dolore magna</span></div>
  <div class="abs bullet" style="left:190px;top:135px;width:100px"><span class="tri" style="border-left-color:#9ad9f5"></span><span>Lorem ipsum dolor sit amet, consectetuer adipiscing elit, sed diam nonummy nibh euismod tincidunt ut laoreet dolore magna</span></div>
  <div class="baseline"></div><div class="mark">VELORA SYSTEMS GROUP <i>04</i></div>
</section>

<!-- 5 education -->
<section class="slide">
  <div class="abs" style="left:11px;top:12px;font-size:11px;line-height:1"><span class="kicker" style="font-size:11px">Our company </span><span class="head" style="font-size:11px">Education</span></div>
  <svg class="abs" style="left:48px;top:38px" width="210" height="90" viewBox="0 0 210 90">
    <rect x="2" y="2" width="54" height="80" rx="5" fill="none" stroke="var(--sky)" stroke-width="1.6"/>
    <rect x="76" y="2" width="54" height="80" rx="5" fill="none" stroke="var(--violet)" stroke-width="1.6"/>
    <rect x="150" y="2" width="54" height="80" rx="5" fill="none" stroke="var(--sky)" stroke-width="1.6"/>
    <path d="M56 22 C70 22 62 60 76 60" fill="none" stroke="var(--violet)" stroke-width="1.6"/>
    <path d="M130 22 C144 22 136 60 150 60" fill="none" stroke="var(--violet)" stroke-width="1.6"/>
    <circle cx="56" cy="22" r="3" fill="var(--sky)"/><circle cx="76" cy="60" r="3" fill="var(--violet)"/>
    <circle cx="130" cy="22" r="3" fill="var(--violet)"/><circle cx="150" cy="60" r="3" fill="var(--sky)"/>
    <g fill="none" stroke="var(--ink)" stroke-width=".8">
      <circle cx="29" cy="18" r="4"/><path d="M27 23h4M27.5 25h3"/>
      <rect x="98" y="15" width="10" height="7"/><path d="M98 15l5 4 5-4"/>
      <path d="M171 14v10h10M173 21l3-3 2 2 3-4"/>
    </g>
  </svg>
  <div class="abs" style="left:50px;top:67px;width:54px;text-align:center;font-size:4.6px;font-weight:600">IDEA</div>
  <div class="abs" style="left:124px;top:67px;width:54px;text-align:center;font-size:4.6px;font-weight:600">PROMOTION</div>
  <div class="abs" style="left:198px;top:67px;width:54px;text-align:center;font-size:4.6px;font-weight:600">GROWTH</div>
  <div class="abs p" style="left:54px;top:74px;width:46px;text-align:center;font-size:2.8px;line-height:3.5px">Lorem ipsum dolor sit amet, consectetuer adipiscing elit, sed diam nonummy nibh euismod tincidunt ut laoreet dolore magna aliquam erat volutpat. Ut wisi enim ad minim veniam, quis nostrud exerci tation</div>
  <div class="abs p" style="left:128px;top:74px;width:46px;text-align:center;font-size:2.8px;line-height:3.5px">Lorem ipsum dolor sit amet, consectetuer adipiscing elit, sed diam nonummy nibh euismod tincidunt ut laoreet dolore magna aliquam erat volutpat. Ut wisi enim ad minim veniam, quis nostrud exerci tation</div>
  <div class="abs p" style="left:202px;top:74px;width:46px;text-align:center;font-size:2.8px;line-height:3.5px">Lorem ipsum dolor sit amet, consectetuer adipiscing elit, sed diam nonummy nibh euismod tincidunt ut laoreet dolore magna aliquam erat volutpat. Ut wisi enim ad minim veniam, quis nostrud exerci tation</div>
  <div class="abs p" style="left:32px;top:135px;width:242px;text-align:center">Lorem ipsum dolor sit amet, consectetuer adipiscing elit, sed diam nonummy nibh euismod tincidunt ut laoreet dolore magna aliquam erat volutpat. Ut wisi enim ad minim veniam, quis nostrud exerci tation ullamcorper suscipit lobortis nisl ut aliquip ex ea commodo consequat. Duis autem vel eum iriure dolor in hendrerit i</div>
  <div class="baseline"></div><div class="mark">VELORA SYSTEMS GROUP <i>05</i></div>
</section>

<!-- 6 domain -->
<section class="slide">
  <div class="abs kicker" style="left:20px;top:22px;font-size:10px">Lorem ipsum</div>
  <div class="abs head" style="left:20px;top:34px;font-size:10px">Dolor sit amet</div>
  <div class="abs p" style="left:20px;top:49px;width:135px">Lorem ipsum dolor sit amet, consectetuer adipiscing elit, sed diam nonummy nibh euismod tincidunt ut laoreet dolore magna aliquam erat volutpat. Ut wisi enim ad minim veniam, quis nostrud exerci tation ullamcorper suscipit lobortis nisl ut aliquip ex ea commodo consequat. Duis autem vel eum iriure dolor in hendrerit in vulputate velit esse</div>
  <div class="abs p" style="left:20px;top:84px;width:135px">Lorem ipsum dolor sit amet, consectetuer adipiscing elit, sed diam nonummy nibh euismod tincidunt ut laoreet dolore magna aliquam erat volutpat. Ut wisi enim ad minim</div>
  <div class="abs bullet" style="left:20px;top:107px;width:135px"><span class="tri"></span><span>Lorem ipsum dolor sit amet, consectetuer adipiscing elit, sed diam nonummy nibh euismod tincidunt ut laoreet dolore magna</span></div>
  <div class="abs bullet" style="left:20px;top:126px;width:135px"><span class="tri" style="border-left-color:#9ad9f5"></span><span>Lorem ipsum dolor sit amet, consectetuer adipiscing elit, sed diam nonummy nibh euismod tincidunt ut laoreet dolore magna</span></div>
  <div class="abs kicker" style="left:170px;top:22px;font-size:8px;line-height:12px">What's a domain?<br>It's that name up</div>
  <div class="abs head" style="left:170px;top:47px;font-size:8px">In the address bar.</div>
  <ul class="abs" style="left:170px;top:61px;list-style:none;font-size:6px;line-height:12.7px;color:var(--text)">
    <li><span style="color:var(--violet);margin-right:6px">✓</span>Fits your business or products</li>
    <li><span style="color:var(--violet);margin-right:6px">✓</span>Is easy to spell and remember</li>
    <li><span style="color:var(--violet);margin-right:6px">✓</span>Fits your business or products</li>
    <li><span style="color:var(--violet);margin-right:6px">✓</span>Is easy to spell and remember</li>
    <li><span style="color:var(--violet);margin-right:6px">✓</span>Fits your business or products</li>
    <li><span style="color:var(--violet);margin-right:6px">✓</span>Is easy to spell and remember</li>
  </ul>
  <div class="baseline"></div><div class="mark">VELORA SYSTEMS GROUP <i>06</i></div>
</section>

<!-- 7 overview -->
<section class="slide">
  <div class="abs kicker" style="left:15px;top:18px;font-size:10px;font-weight:600">Company</div>
  <div class="abs head" style="left:15px;top:30px;font-size:14px">Overview</div>
  <div class="abs p" style="left:15px;top:49px;width:120px">Lorem ipsum dolor sit amet, consectetuer adipiscing elit, sed diam nonummy nibh euismod tincidunt ut laoreet dolore magna aliquam erat volutpat. Ut wisi enim ad minim veniam, quis nostrud exerci tation ullamcorper suscipit lobortis nisl ut aliquip ex ea commodo consequat. Duis autem vel eum iriure dolor in hendrerit i</div>
  <div class="abs p" style="left:15px;top:76px;width:120px">Lorem ipsum dolor sit amet, consectetuer adipiscing elit, sed diam nonummy nibh</div>
  <svg class="abs" style="left:148px;top:12px" width="150" height="82" viewBox="0 0 150 82" font-family="Poppins,sans-serif" font-size="4" fill="#555">
    <g stroke="#ddd" stroke-width=".4"><path d="M10 4h135M10 14.5h135M10 25h135M10 35.5h135M10 46h135M10 56.5h135"/><path d="M10 67h135" stroke="#999"/></g>
    <text x="0" y="5.5">60</text><text x="0" y="16">50</text><text x="0" y="26.5">40</text><text x="0" y="37">30</text><text x="0" y="47.5">20</text><text x="0" y="58">10</text><text x="3" y="68.5">0</text>
    <rect x="21" y="25" width="4" height="42" fill="var(--cyan)"/><rect x="26" y="14.5" width="4" height="52.5" fill="var(--violet)"/>
    <rect x="48" y="55.5" width="4" height="11.5" fill="var(--cyan)"/><rect x="53" y="30" width="4" height="37" fill="var(--violet)"/>
    <rect x="75" y="6" width="4" height="61" fill="var(--cyan)"/><rect x="80" y="53" width="4" height="14" fill="var(--violet)"/>
    <rect x="108" y="12.5" width="4" height="54.5" fill="var(--violet)"/><rect x="113" y="35.5" width="4" height="31.5" fill="var(--cyan)"/>
    <text x="21" y="76">JAN</text><text x="49" y="76">FEB</text><text x="76" y="76">MAR</text><text x="108" y="76">APR</text>
  </svg>
  <svg class="abs" style="left:12px;top:98px" width="125" height="62" viewBox="0 0 125 62" font-family="Poppins,sans-serif" font-size="3" fill="#555">
    <g stroke="#ddd" stroke-width=".4"><path d="M10 4h112M10 11h112M10 18h112M10 25h112M10 32h112M10 39h112"/><path d="M10 46h112" stroke="#999"/></g>
    <text x="0" y="5">60</text><text x="0" y="12">50</text><text x="0" y="19">40</text><text x="0" y="26">30</text><text x="0" y="33">20</text><text x="0" y="40">10</text><text x="3" y="47">0</text>
    <polyline points="14,40 26,33 38,18 50,30 62,12 74,24 86,15 98,26 110,18" fill="none" stroke="var(--violet)" stroke-width=".7"/>
    <polyline points="14,40 26,38 38,28 50,10 62,14 74,30 86,22 98,20 110,40" fill="none" stroke="var(--cyan)" stroke-width=".7"/>
    <g font-size="2.3" text-anchor="middle"><text x="14" y="53">TEXT 01</text><text x="26" y="53">TEXT 02</text><text x="38" y="53">TEXT 03</text><text x="50" y="53">TEXT 04</text><text x="62" y="53">TEXT 05</text><text x="74" y="53">TEXT 06</text><text x="86" y="53">TEXT 07</text><text x="98" y="53">TEXT 08</text><text x="110" y="53">TEXT 09</text></g>
  </svg>
  <div class="abs" style="left:148px;top:106px;display:grid;grid-template-columns:76px 60px;row-gap:8px">
    <div class="legend"><b style="background:var(--violet)"></b><div><div class="lbl">Lorem ipsum</div><div class="p" style="font-size:2.7px;line-height:3.4px">Lorem ipsum dolor sit amet, consec-tetuer adipiscing elit, sed diam nonummy nibh euismod tincid</div></div></div>
    <div class="legend"><b style="background:var(--cyan)"></b><div><div class="lbl">Lorem ipsum</div><div class="p" style="font-size:2.7px;line-height:3.4px">Lorem ipsum dolor sit amet, consec-tetuer adipiscing elit, sed diam nonummy nibh euismod tincid</div></div></div>
    <div class="legend"><b style="background:var(--cyan)"></b><div><div class="lbl">Lorem ipsum</div><div class="p" style="font-size:2.7px;line-height:3.4px">Lorem ipsum dolor sit amet, consec-tetuer adipiscing elit, sed diam nonummy nibh euismod tincid</div></div></div>
    <div class="legend"><b style="background:var(--violet)"></b><div><div class="lbl">Lorem ipsum</div><div class="p" style="font-size:2.7px;line-height:3.4px">Lorem ipsum dolor sit amet, consec-tetuer adipiscing elit, sed diam nonummy nibh euismod tincid</div></div></div>
  </div>
  <div class="baseline"></div><div class="mark">VELORA SYSTEMS GROUP <i>07</i></div>
</section>

<!-- 8 portfolio -->
<section class="slide">
  <div class="abs kicker" style="left:17px;top:21px;font-size:7.5px">Portfolio of</div>
  <div class="abs head" style="left:17px;top:30px;font-size:14px">Projects</div>
  <div class="abs p" style="left:17px;top:47px;width:100px">Lorem ipsum dolor sit amet, consectetuer adipiscing elit, sed diam nonummy nibh euismod tincidunt ut laoreet dolore magna aliquam erat volutpat. Ut wisi enim ad minim veniam, quis nostrud exerci tation ullamcorper suscipit lobortis nisl ut aliquip ex ea commodo consequat. Duis autem vel eum iriure dolor in hendrerit in vulputate velit esse</div>
  <div class="abs p" style="left:17px;top:82px;width:100px">Lorem ipsum dolor sit amet, consectetuer adipiscing elit, sed diam nonummy nibh euismod tincidunt ut laoreet dolore magna aliquam erat volutpat. Ut wisi enim ad minim veniam, quis nostrud exerci tation ullamcorper suscipit lobortis nisl ut aliquip ex ea commodo consequat. Duis autem vel eum iriure dolor in hendrerit in vulputate velit esse</div>
  <div class="abs bullet" style="left:17px;top:117px;width:100px"><span class="tri" style="border-left-color:var(--violet)"></span><span>Lorem ipsum dolor sit amet, consectetuer adipiscing elit, sed diam nonummy nibh euismod tincidunt ut laoreet dolore magna</span></div>
  <div class="abs bullet" style="left:17px;top:136px;width:100px"><span class="tri" style="border-left-color:#b9acf2"></span><span>Lorem ipsum dolor sit amet, consectetuer adipiscing elit, sed diam nonummy nibh euismod tincidunt ut laoreet dolore magna</span></div>
  <div class="abs" style="left:211px;top:20px;width:56px;height:2px;background:var(--violet)"></div>
  <div class="abs" style="left:265px;top:20px;width:2px;height:40px;background:var(--violet)"></div>
  <div class="abs" style="left:131px;top:132px;width:2px;height:30px;background:var(--cyan)"></div>
  <div class="abs" style="left:131px;top:160px;width:56px;height:2px;background:var(--cyan)"></div>
  <div class="art" role="img" aria-label="Photo of a person using a tablet with glowing circuit and icon overlays" style="left:138px;top:27px;width:121px;height:128px;background:linear-gradient(135deg,#c7d3f3,#5a84e0 50%,#23307e)"></div>
  <div class="baseline"></div><div class="mark">VELORA SYSTEMS GROUP <i>08</i></div>
</section>

<!-- 9 scope -->
<section class="slide">
  <div class="abs" style="left:17px;top:22px;font-size:10px;line-height:1"><span class="kicker" style="font-size:8px;font-weight:600">Company </span><span class="head" style="font-size:11px">Scope</span></div>
  <div class="abs p" style="left:17px;top:42px;width:105px;font-size:4px;line-height:5px;text-align:left">Lorem ipsum dolor sit amet, consectetuer adipiscing elit, sed diam nonummy nibh euis-mod tincidunt ut laoreet dolore</div>
  <svg class="abs" style="left:14px;top:82px" width="115" height="80" viewBox="0 0 115 80" font-family="Poppins,sans-serif" font-weight="700" fill="#fff" text-anchor="middle">
    <g transform="translate(57,38) scale(1,0.62)">
      <g transform="translate(0,14)" fill="none" stroke-width="20">
        <circle r="40" stroke="#0d8fb8" stroke-dasharray="100.5 150.8" transform="rotate(90)"/>
        <circle r="40" stroke="#1f1770" stroke-dasharray="50.3 201" transform="rotate(18)"/>
        <circle r="40" stroke="#0d8fb8" stroke-dasharray="50.3 201" transform="rotate(-54)"/>
      </g>
      <g fill="none" stroke-width="20">
        <circle r="40" stroke="var(--cyan)" stroke-dasharray="100.5 150.8" transform="rotate(90)"/>
        <circle r="40" stroke="var(--violet)" stroke-dasharray="50.3 201" transform="rotate(-126)"/>
        <circle r="40" stroke="var(--sky)" stroke-dasharray="50.3 201" transform="rotate(-54)"/>
        <circle r="40" stroke="var(--deep)" stroke-dasharray="50.3 201" transform="rotate(18)"/>
      </g>
    </g>
    <text x="19" y="48" font-size="7.5">40%</text>
    <text x="57" y="16" font-size="6.5">20%</text>
    <text x="95" y="33" font-size="6.5">20%</text>
    <text x="80" y="61" font-size="6.5">20%</text>
  </svg>
  <div class="abs" style="left:160px;top:13px;font-size:4.2px;font-weight:600">CONSECTETUER ADIPISCING</div>
  <svg class="abs" style="left:160px;top:22px" width="135" height="75" viewBox="0 0 135 75" font-family="Poppins,sans-serif" font-size="3.8" fill="#555">
    <g stroke="#ddd" stroke-width=".4"><path d="M10 3h120M10 12h120M10 21h120M10 30h120M10 39h120M10 48h120"/><path d="M10 57h120" stroke="#999"/></g>
    <text x="1" y="4.5">60</text><text x="1" y="13.5">50</text><text x="1" y="22.5">40</text><text x="1" y="31.5">30</text><text x="1" y="40.5">20</text><text x="1" y="49.5">10</text><text x="4" y="58.5">0</text>
    <rect x="18" y="21" width="13" height="36" fill="var(--violet)"/><rect x="43" y="3" width="13" height="54" fill="var(--cyan)"/>
    <rect x="68" y="43.5" width="13" height="13.5" fill="var(--violet)"/><rect x="93" y="15" width="13" height="42" fill="var(--cyan)"/>
    <text x="19" y="66">JAN</text><text x="45" y="66">FEB</text><text x="69" y="66">MAR</text><text x="95" y="66">APR</text>
  </svg>
  <div class="abs" style="left:146px;top:98px;display:grid;grid-template-columns:78px 70px;row-gap:8px">
    <div class="legend"><b style="background:var(--violet)"></b><div><div class="lbl">Lorem ipsum</div><div class="p" style="font-size:2.7px;line-height:3.4px">Lorem ipsum dolor sit amet, consectetuer adipiscing elit, sed diam nonummy nibh euismod tincidunt ut laoreet</div></div></div>
    <div class="legend"><b style="background:var(--cyan)"></b><div><div class="lbl" style="color:var(--cyan)">Lorem ipsum</div><div class="p" style="font-size:2.7px;line-height:3.4px">Lorem ipsum dolor sit amet, consectetuer adipiscing elit, sed diam nonummy nibh euismod tincidunt ut laoreet</div></div></div>
    <div class="legend"><b style="background:var(--cyan)"></b><div><div class="lbl" style="color:var(--cyan)">Lorem ipsum</div><div class="p" style="font-size:2.7px;line-height:3.4px">Lorem ipsum dolor sit amet, consectetuer adipiscing elit, sed diam nonummy nibh euismod tincidunt ut laoreet</div></div></div>
    <div class="legend"><b style="background:var(--violet)"></b><div><div class="lbl">Lorem ipsum</div><div class="p" style="font-size:2.7px;line-height:3.4px">Lorem ipsum dolor sit amet, consectetuer adipiscing elit, sed diam nonummy nibh euismod tincidunt ut laoreet</div></div></div>
  </div>
  <div class="baseline"></div><div class="mark">VELORA SYSTEMS GROUP <i>09</i></div>
</section>

<!-- 10 lorem dolor with icons -->
<section class="slide">
  <div class="abs kicker" style="left:19px;top:25px;font-size:10px">Lorem ipsum</div>
  <div class="abs head" style="left:19px;top:37px;font-size:10px">Dolor sit amet</div>
  <div class="abs p" style="left:19px;top:51px;width:138px">Lorem ipsum dolor sit amet, consectetuer adipiscing elit, sed diam nonummy nibh euismod tincidunt ut laoreet dolore magna aliquam erat volutpat. Ut wisi enim ad minim veniam, quis nostrud exerci tation ullamcorper suscipit lobortis nisl ut aliquip ex ea commodo consequat. Duis autem vel eum iriure dolor in hendrerit in vulputate velit esse molestie consequat, vel illum dolore eu feugiat nulla facilisis at vero eros et accumsan et iusto odio dignissim qui blandit praesent luptatum zzril delenit augue duis dolore te feugait nulla facilisi.</div>
  <div class="abs p" style="left:19px;top:97px;width:138px">Lorem ipsum dolor sit amet, cons ectetuer adipiscing elit, sed diam nonummy nibh euismod tincidunt ut laoreet dolore magna aliquam erat volutpat. Ut wisi enim ad minim veniam, quis nostrud exerci tation ullamcorper suscipit lobortis nisl ut aliquip ex ea commodo consequat.</div>
  <div class="abs p" style="left:19px;top:122px;width:138px">Lorem ipsum dolor sit amet, consectetuer adipiscing elit, sed diam nonummy nibh euismod tincidunt ut laoreet dolore magna aliquam erat volutpat. Ut wisi enim ad minim veniam, quis nostrud exerci tation ullamcorper suscipit lobortis nisl ut aliquip ex ea commodo consequat. Duis autem vel eum iriure dolor in hendrerit in vulputate velit esse molestie</div>
  <div class="abs" style="left:178px;top:38px;display:grid;grid-template-columns:58px 58px;row-gap:8px;text-align:center">
    <div><span style="display:block;margin:0 auto 4px;width:22px;height:22px;border-radius:50%;border:1px solid var(--cyan);box-shadow:inset 0 0 0 3px #fff,inset 0 0 0 4px #c9c2f4"></span><div class="lbl" style="font-size:4.4px">LOREM IPSUM</div><div class="p" style="text-align:center;font-size:2.8px;line-height:3.5px">Lorem ipsum dolor sit amet, consectetuer adipiscing elit, sed diam nonummy nibh euismod tincid</div></div>
    <div><span style="display:block;margin:0 auto 4px;width:22px;height:22px;border-radius:50%;border:1px solid var(--cyan);box-shadow:inset 0 0 0 3px #fff,inset 0 0 0 4px #c9c2f4"></span><div class="lbl" style="font-size:4.4px">LOREM IPSUM</div><div class="p" style="text-align:center;font-size:2.8px;line-height:3.5px">Lorem ipsum dolor sit amet, consectetuer adipiscing elit, sed diam nonummy nibh euismod tincid</div></div>
    <div><span style="display:block;margin:0 auto 4px;width:22px;height:22px;border-radius:50%;border:1px solid var(--cyan);box-shadow:inset 0 0 0 3px #fff,inset 0 0 0 4px #c9c2f4"></span><div class="lbl" style="font-size:4.4px">LOREM IPSUM</div><div class="p" style="text-align:center;font-size:2.8px;line-height:3.5px">Lorem ipsum dolor sit amet, consectetuer adipiscing elit, sed diam nonummy nibh euismod tincid</div></div>
    <div><span style="display:block;margin:0 auto 4px;width:22px;height:22px;border-radius:50%;border:1px solid var(--cyan);box-shadow:inset 0 0 0 3px #fff,inset 0 0 0 4px #c9c2f4"></span><div class="lbl" style="font-size:4.4px">LOREM IPSUM</div><div class="p" style="text-align:center;font-size:2.8px;line-height:3.5px">Lorem ipsum dolor sit amet, consectetuer adipiscing elit, sed diam nonummy nibh euismod tincid</div></div>
  </div>
  <div class="baseline"></div><div class="mark">VELORA SYSTEMS GROUP <i>10</i></div>
</section>

<!-- 11 use cases -->
<section class="slide">
  <div class="art" role="img" aria-label="Illustration of three stepped smartphone screens with short course notes over faint orbit lines" style="left:20px;top:20px;width:135px;height:128px;border-radius:6px;background:linear-gradient(160deg,#f4f4f7,#e4e5ec 60%,#f7f7fa)"></div>
  <div class="abs" style="left:166px;top:47px;font-size:18px;line-height:1"><span class="kicker" style="font-size:18px;font-weight:400">Use </span><span class="head" style="font-size:18px">Cases</span></div>
  <div class="abs p" style="left:166px;top:73px;width:124px">Lorem ipsum dolor sit amet, consectetuer adipiscing elit, sed diam nonummy nibh euismod tincidunt ut laoreet dolore magna aliquam erat volutpat. Ut wisi enim ad minim veniam, quis nostrud exerci tation ullamcorper suscipit lobortis nisl ut aliquip ex ea commodo consequat. Duis autem vel eum iriure dolor in hendrerit i</div>
  <div class="abs p" style="left:166px;top:108px;width:124px">Lorem ipsum dolor sit amet, consectetuer adipiscing elit, sed diam nonummy nibh euismod tincidunt ut laoreet dolore magna aliquam erat volutpat. Ut wisi enim ad minim veniam, quis nostrud exerci tation ullamcorper suscipit lobortis nisl ut aliquip ex ea commodo consequat. Duis autem vel eum iriure dolor in hendrerit in</div>
  <div class="baseline"></div><div class="mark">VELORA SYSTEMS GROUP <i>11</i></div>
</section>

<!-- 12 costs -->
<section class="slide">
  <div class="abs" style="left:0;right:0;top:14px;text-align:center;font-size:14px;line-height:1"><span class="kicker" style="font-size:14px;font-weight:400">Company </span><span class="head" style="font-size:14px">Costs</span></div>
  <div class="abs p" style="left:18px;top:32px;width:270px;text-align:center">Lorem ipsum dolor sit amet, consectetuer adipiscing elit, sed diam nonummy nibh euismod tincidunt ut laoreet dolore magna aliquam erat volut-pat. Ut wisi enim ad minim veniam, quis nostrud exerci tation ullamcorper suscipit lobortis nisl ut aliquip ex ea commodo consequat.</div>
  <div class="abs p" style="left:18px;top:45px;width:270px;text-align:center">Duis autem vel eum iriure dolor in hendrerit in vulputate velit esse molestie consequat, vel illum dolore eu feugiat nulla facilisis at vero eros et accumsan et iusto odio dignissim qui blandit praesent luptatum zzril delenit augue duis dolore te feugait nulla facilisi</div>
  <svg class="abs" style="left:0;top:60px" width="305" height="70" viewBox="0 0 305 70" font-family="Poppins,sans-serif" font-size="3.6" font-weight="600" fill="#fff">
    <rect x="20" y="37" width="262" height="3" fill="var(--cyan)"/>
    <rect x="140" y="37" width="142" height="3" fill="var(--violet)"/>
    <path d="M282 34.5l7 4-7 4z" fill="var(--violet)"/>
    <g fill="none" stroke-width="5">
      <path d="M60 37 A 15 15 0 1 1 90 37" stroke="var(--cyan)"/>
      <path d="M113 37 A 15 15 0 1 1 143 37" stroke="var(--violet)"/>
      <path d="M166 37 A 15 15 0 1 1 196 37" stroke="var(--cyan)"/>
      <path d="M219 37 A 15 15 0 1 1 249 37" stroke="var(--violet)"/>
    </g>
    <g fill="#fff"><circle cx="75" cy="26" r="7"/><circle cx="128" cy="26" r="7"/><circle cx="181" cy="26" r="7"/><circle cx="234" cy="26" r="7"/></g>
    <g fill="none" stroke="var(--deep)" stroke-width=".9">
      <circle cx="75" cy="26" r="4"/><path d="M75 23.5v2.5h2"/>
      <ellipse cx="181" cy="23.5" rx="3.5" ry="1.3"/><path d="M177.5 23.5v5c0 1.7 7 1.7 7 0v-5M177.5 26c0 1.7 7 1.7 7 0"/>
      <circle cx="233" cy="25" r="3"/><path d="M235 27l2.5 2.5"/>
    </g>
    <circle cx="128" cy="26" r="4" fill="var(--deep)"/><text x="126.3" y="27.5" font-size="4.5">$</text>
    <text x="78" y="44.5">Step 01</text><text x="131" y="44.5">Step 02</text><text x="184" y="44.5">Step 03</text><text x="237" y="44.5">Step 04</text>
    <g stroke="#999" stroke-width=".5"><path d="M75 46v12M128 46v12M181 46v12M234 46v12"/></g>
    <g fill="#999"><circle cx="75" cy="58" r="1"/><circle cx="128" cy="58" r="1"/><circle cx="181" cy="58" r="1"/><circle cx="234" cy="58" r="1"/></g>
  </svg>
  <div class="abs" style="left:52px;top:122px;display:grid;grid-template-columns:repeat(4,46px);column-gap:7px;text-align:center">
    <div><div class="lbl" style="color:var(--cyan)">Lorem Ipsum</div><div class="p" style="text-align:center;font-size:2.6px;line-height:3.3px">Lorem ipsum dolor sit amet, consectetuer adipiscing elit, sed diam nonummy nibh euismod tincidunt ut laoreet dolore magna aliquam erat volutpat. Ut wisi</div></div>
    <div><div class="lbl">Lorem Ipsum</div><div class="p" style="text-align:center;font-size:2.6px;line-height:3.3px">Lorem ipsum dolor sit amet, consectetuer adipiscing elit, sed diam nonummy nibh euismod tincidunt ut laoreet dolore magna aliquam erat volutpat. Ut wisi</div></div>
    <div><div class="lbl" style="color:var(--cyan)">Lorem Ipsum</div><div class="p" style="text-align:center;font-size:2.6px;line-height:3.3px">Lorem ipsum dolor sit amet, consectetuer adipiscing elit, sed diam nonummy nibh euismod tincidunt ut laoreet dolore magna aliquam erat volutpat. Ut wisi</div></div>
    <div><div class="lbl">Lorem Ipsum</div><div class="p" style="text-align:center;font-size:2.6px;line-height:3.3px">Lorem ipsum dolor sit amet, consectetuer adipiscing elit, sed diam nonummy nibh euismod tincidunt ut laoreet dolore magna aliquam erat volutpat. Ut wisi</div></div>
  </div>
  <div class="baseline"></div><div class="mark">VELORA SYSTEMS GROUP <i>12</i></div>
</section>

<!-- 13 roadmap -->
<section class="slide">
  <div class="abs" style="left:0;top:16px;width:93px;height:31px;background:var(--cyan);color:#fff;font-size:8.5px;font-weight:600;line-height:11px;padding:5px 0 0 15px">TIMELINE OF<br>ROADMAP</div>
  <div class="abs" style="left:23px;top:64px;font-size:8.5px;font-weight:600;color:var(--violet)">FOR <span style="color:var(--violet)">2 YEARS</span></div>
  <div class="abs" style="left:24px;top:80px;display:flex;gap:5px;align-items:flex-start">
    <span style="flex:none;width:19px;height:19px;border-radius:50%;background:var(--violet);border:1.5px solid #c9c2f4;color:#fff;font-size:10px;font-weight:700;display:flex;align-items:center;justify-content:center">A</span>
    <div><div style="font-size:9px;font-weight:500;color:var(--violet);line-height:1">2019</div><div class="p" style="width:38px;text-align:left;font-size:2.6px;line-height:3.4px;margin-top:2px">Lorem ipsum dolor sit amet, consectetuer adipiscing elit, sed diam</div></div>
  </div>
  <div class="abs" style="left:24px;top:115px;display:flex;gap:5px;align-items:flex-start">
    <span style="flex:none;width:19px;height:19px;border-radius:50%;background:var(--violet);border:1.5px solid #c9c2f4;color:#fff;font-size:10px;font-weight:700;display:flex;align-items:center;justify-content:center">B</span>
    <div><div style="font-size:9px;font-weight:500;color:var(--violet);line-height:1">2020</div><div class="p" style="width:38px;text-align:left;font-size:2.6px;line-height:3.4px;margin-top:2px">Lorem ipsum dolor sit amet, consectetuer adipiscing elit, sed diam</div></div>
  </div>
  <div class="art" role="img" aria-label="3D winding road with three numbered milestone markers" style="left:108px;top:18px;width:175px;height:86px;border-radius:6px;background:linear-gradient(110deg,#e1e3ea,#9da2b3 45%,#dff4fb)"></div>
  <div class="option" style="left:178px;top:38px"><b>OPTION</b></div>
  <div class="option" style="left:223px;top:59px"><b>OPTION</b></div>
  <div class="option" style="left:251px;top:83px"><b>OPTION</b></div>
  <div class="abs" style="left:110px;top:112px;font-size:8.5px;font-weight:700;color:var(--ink)">+3467</div>
  <div class="abs" style="left:111px;top:125px;font-size:5px;font-weight:600;font-style:italic;line-height:6px;color:var(--ink)">Lorem ipsum<br>dolor sit amet elit,</div>
  <div class="baseline"></div><div class="mark">VELORA SYSTEMS GROUP <i>13</i></div>
</section>

<!-- 14 benefits -->
<section class="slide">
  <div class="art" role="img" aria-label="Isometric illustration of a friendly robot standing on an AI chip with circuit traces" style="left:18px;top:18px;width:125px;height:130px;background:radial-gradient(ellipse at 50% 60%,#cde9fb,#eef0fd 55%,#fff 75%)"></div>
  <div class="abs kicker" style="left:150px;top:15px;font-size:10px;font-weight:500">Benefits to each</div>
  <div class="abs head" style="left:150px;top:27px;font-size:10px">Customer Segments</div>
  <div class="abs" style="left:150px;top:42px;width:140px;display:flex;flex-direction:column;gap:3px">
    <div class="p">Lorem ipsum dolor sit amet, consectetuer adipiscing elit, sed diam nonummy nibh euismod tincidunt ut laoreet dolore magna aliquam erat volutpat. Ut wisi enim ad minim veniam, quis nostrud exerci tation ullam</div>
    <div class="p">Lorem ipsum dolor sit amet, consectetuer adipiscing elit, sed diam nonummy nibh euismod tincidunt ut laoreet dolore magna aliquam erat volutpat. Ut wisi enim ad minim veniam, quis nostrud exerci tation ullam</div>
    <div class="p">Lorem ipsum dolor sit amet, consectetuer adipiscing elit, sed diam nonummy nibh euismod tincidunt ut laoreet dolore magna aliquam erat volutpat. Ut wisi enim ad minim veniam, quis nostrud exerci tation ullam</div>
    <div class="p">Lorem ipsum dolor sit amet, consectetuer adipiscing elit, sed diam nonummy nibh euismod tincidunt ut laoreet dolore magna aliquam erat volutpat. Ut wisi enim ad minim veniam, quis nostrud exerci tation ullam Lorem ipsum dolor sit amet, consectetuer adipiscing elit, sed diam nonummy nibh euismod tincidunt ut laoreet dolore magna aliquam erat volutpat. Ut wisi enim ad minim veniam, quis nostrud exerci</div>
  </div>
  <div class="baseline"></div><div class="mark">VELORA SYSTEMS GROUP <i>14</i></div>
</section>

<!-- 15 advisors -->
<section class="slide">
  <div class="abs" style="left:107px;top:13px;width:93px;height:137px;background:var(--panel)"></div>
  <div class="abs" style="left:16px;top:23px;width:276px;display:grid;grid-template-columns:repeat(3,82px);column-gap:15px">
    <div><div class="kicker" style="font-size:7px;text-align:center">Active advisors</div><div class="head" style="font-size:9px;text-align:center;margin-top:2px">And members</div><div style="height:1px;background:var(--cyan);margin:3px 0 4px"></div><div class="p">Lorem ipsum dolor sit amet, consectetuer adipiscing elit, sed diam nonummy nibh euismod tincidunt ut laoreet dolore magna aliquam erat volutpat. Ut wisi enim ad minim veniam, quis nostrud exerci tation ullamcorper suscipit lobortis nisl ut aliquip ex ea commodo consequat. Duis autem vel eum iriure dolor in hendrerit in vulputate velit esse</div><div class="p" style="margin-top:3px">Lorem ipsum dolor sit amet, consectetuer adipiscing elit, sed diam nonummy nibh euismod tincidunt ut laoreet dolore magna aliquam erat volutpat. Ut wisi enim ad minim veniam, quis nostrud exerci tation ullamcorper suscipit lobortis nisl ut aliquip ex ea commodo consequat. Duis autem vel eum iriure dolor in hendrerit in vulputate velit esse</div><div class="p" style="margin-top:3px">Lorem ipsum dolor sit amet, consectetuer adipiscing elit, sed diam nonummy nibh euismod tincidunt ut laoreet dolore magna aliquam erat volutpat. Ut wisi enim ad minim veniam, quis nostrud exerci Lorem ipsum dolor sit amet, consectetuer adipiscing elit, sed diam nonummy nibh euismod tincidunt</div></div>
    <div><div class="kicker" style="font-size:7px;text-align:center">Active advisors</div><div class="head" style="font-size:9px;text-align:center;margin-top:2px">And members</div><div style="height:1px;background:var(--cyan);margin:3px 0 4px"></div><div class="p">Lorem ipsum dolor sit amet, consectetuer adipiscing elit, sed diam nonummy nibh euismod tincidunt ut laoreet dolore magna aliquam erat volutpat. Ut wisi enim ad minim veniam, quis nostrud exerci tation ullamcorper suscipit lobortis nisl ut aliquip ex ea commodo consequat. Duis autem vel eum iriure dolor in hendrerit in vulputate velit esse</div><div class="p" style="margin-top:3px">Lorem ipsum dolor sit amet, consectetuer adipiscing elit, sed diam nonummy nibh euismod tincidunt ut laoreet dolore magna aliquam erat volutpat. Ut wisi enim ad minim veniam, quis nostrud exerci tation ullamcorper suscipit lobortis nisl ut aliquip ex ea commodo consequat. Duis autem vel eum iriure dolor in hendrerit in vulputate velit esse</div><div class="p" style="margin-top:3px">Lorem ipsum dolor sit amet, consectetuer adipiscing elit, sed diam nonummy nibh euismod tincidunt ut laoreet dolore magna aliquam erat volutpat. Ut wisi enim ad minim veniam, quis nostrud exerci Lorem ipsum dolor sit amet, consectetuer adipiscing elit, sed diam nonummy nibh euismod tincidunt</div></div>
    <div><div class="kicker" style="font-size:7px;text-align:center">Active advisors</div><div class="head" style="font-size:9px;text-align:center;margin-top:2px">And members</div><div style="height:1px;background:var(--cyan);margin:3px 0 4px"></div><div class="p">Lorem ipsum dolor sit amet, consectetuer adipiscing elit, sed diam nonummy nibh euismod tincidunt ut laoreet dolore magna aliquam erat volutpat. Ut wisi enim ad minim veniam, quis nostrud exerci tation ullamcorper suscipit lobortis nisl ut aliquip ex ea commodo consequat. Duis autem vel eum iriure dolor in hendrerit in vulputate velit esse</div><div class="p" style="margin-top:3px">Lorem ipsum dolor sit amet, consectetuer adipiscing elit, sed diam nonummy nibh euismod tincidunt ut laoreet dolore magna aliquam erat volutpat. Ut wisi enim ad minim veniam, quis nostrud exerci tation ullamcorper suscipit lobortis nisl ut aliquip ex ea commodo consequat. Duis autem vel eum iriure dolor in hendrerit in vulputate velit esse</div><div class="p" style="margin-top:3px">Lorem ipsum dolor sit amet, consectetuer adipiscing elit, sed diam nonummy nibh euismod tincidunt ut laoreet dolore magna aliquam erat volutpat. Ut wisi enim ad minim veniam, quis nostrud exerci Lorem ipsum dolor sit amet, consectetuer adipiscing elit, sed diam nonummy nibh euismod tincidunt</div></div>
  </div>
  <div class="baseline"></div><div class="mark">VELORA SYSTEMS GROUP <i>15</i></div>
</section>

<!-- 16 terms -->
<section class="slide">
  <div class="abs kicker" style="left:10px;top:44px;font-size:10px;font-weight:600">Company</div>
  <div class="abs head" style="left:10px;top:57px;font-size:10px">Terms &amp; Conditions</div>
  <div class="abs" style="left:10px;top:72px;width:122px;display:flex;flex-direction:column;gap:4px">
    <div class="p">Lorem ipsum dolor sit amet, consectetuer adipiscing elit, sed diam nonummy nibh euismod tincidunt ut laoreet dolore magna aliquam erat volutpat. Ut wisi enim ad minim veniam, quis nostrud exerci tation ullam</div>
    <div class="p">Lorem ipsum dolor sit amet, consectetuer adipiscing elit, sed diam nonummy nibh euismod tincidunt ut laoreet dolore magna aliquam erat volutpat. Ut wisi enim ad minim veniam, quis nostrud exerci tation ullam</div>
    <div class="p">Lorem ipsum dolor sit amet, consectetuer adipiscing elit, sed diam nonummy nibh euismod tincidunt ut laoreet dolore magna aliquam erat volutpat. Ut wisi enim ad minim veniam, quis nostrud</div>
  </div>
  <div class="art" role="img" aria-label="Laptop showing a team meeting scene, framed by curved orbit bands" style="left:140px;top:12px;width:158px;height:146px;border-radius:6px;background:linear-gradient(160deg,#eef0f6,#c9cbd6 55%,#e8e6f7)"></div>
  <div class="baseline"></div><div class="mark">VELORA SYSTEMS GROUP <i>16</i></div>
</section>

<!-- 17 team -->
<section class="slide">
  <div class="abs" style="left:0;right:0;top:22px;text-align:center;font-size:9px;line-height:1"><span class="kicker" style="font-size:9px;font-weight:600">Team members </span><span class="head" style="font-size:9px">and advisors</span></div>
  <div class="abs p" style="left:18px;top:37px;width:270px;text-align:center">Lorem ipsum dolor sit amet, consectetuer adipiscing elit, sed diam nonummy nibh euismod tincidunt ut laoreet dolore magna aliquam erat volutpat. Ut wisi enim ad minim veniam, quis nostrud exerci tation ullamcorper suscipit lobortis nisl ut aliquip ex ea commodo consequat. Duis autem</div>
  <div class="abs p" style="left:18px;top:56px;width:270px;text-align:center">Lorem ipsum dolor sit amet, cons ectetuer adipiscing elit, sed diam nonummy nibh euismod tincidunt ut laoreet dolore magna aliquam erat volutpat.</div>
  <div class="abs" style="left:0;top:71px;width:305px;height:71px;background:var(--cyan)"></div>
  <div class="abs" style="left:18px;top:76px;width:270px;display:grid;grid-template-columns:repeat(4,1fr);text-align:center">
    <div><div role="img" aria-label="Portrait photo of team member" style="margin:0 auto;width:26px;height:26px;border-radius:50%;border:1.5px solid #fff;background:linear-gradient(#e9d7c9,#8a6a5a)"></div><div style="font-size:5px;font-weight:600;color:var(--violet);margin-top:2px">ARON PELL</div><div class="p" style="color:#fff;text-align:center;font-size:2.5px;line-height:3.2px;padding:0 8px">Lorem ipsum dolor sit amet, consectetuer adipiscing elit, sed diam nonummy nibh euismod tincidunt ut laoreet dolore magna aliquam erat volutpat. Ut wisi enim ad minim veniam, quis nostrud</div></div>
    <div><div role="img" aria-label="Portrait photo of team member" style="margin:0 auto;width:26px;height:26px;border-radius:50%;border:1.5px solid #fff;background:linear-gradient(#e4d4c7,#6a4a3f)"></div><div style="font-size:5px;font-weight:600;color:var(--violet);margin-top:2px">DANA REYES</div><div class="p" style="color:#fff;text-align:center;font-size:2.5px;line-height:3.2px;padding:0 8px">Lorem ipsum dolor sit amet, consectetuer adipiscing elit, sed diam nonummy nibh euismod tincidunt ut laoreet dolore magna aliquam erat volutpat. Ut wisi enim ad minim veniam, quis nostrud</div></div>
    <div><div role="img" aria-label="Portrait photo of team member" style="margin:0 auto;width:26px;height:26px;border-radius:50%;border:1.5px solid #fff;background:linear-gradient(#e9d7c9,#8a6a5a)"></div><div style="font-size:5px;font-weight:600;color:var(--violet);margin-top:2px">ARON PELL</div><div class="p" style="color:#fff;text-align:center;font-size:2.5px;line-height:3.2px;padding:0 8px">Lorem ipsum dolor sit amet, consectetuer adipiscing elit, sed diam nonummy nibh euismod tincidunt ut laoreet dolore magna aliquam erat volutpat. Ut wisi enim ad minim veniam, quis nostrud</div></div>
    <div><div role="img" aria-label="Portrait photo of team member" style="margin:0 auto;width:26px;height:26px;border-radius:50%;border:1.5px solid #fff;background:linear-gradient(#e4d4c7,#6a4a3f)"></div><div style="font-size:5px;font-weight:600;color:var(--violet);margin-top:2px">DANA REYES</div><div class="p" style="color:#fff;text-align:center;font-size:2.5px;line-height:3.2px;padding:0 8px">Lorem ipsum dolor sit amet, consectetuer adipiscing elit, sed diam nonummy nibh euismod tincidunt ut laoreet dolore magna aliquam erat volutpat. Ut wisi enim ad minim veniam, quis nostrud</div></div>
  </div>
  <div class="baseline"></div><div class="mark">VELORA SYSTEMS GROUP <i>17</i></div>
</section>

<!-- 18 back cover -->
<section class="slide" style="background:linear-gradient(100deg,var(--sky),#2f7ff0 45%,var(--violet))">
  <div class="art" role="img" aria-label="Photo of a white robot working at a laptop" style="left:160px;top:0;width:145px;height:171px;background:linear-gradient(90deg,rgba(90,63,216,0),rgba(200,210,245,.55) 60%,rgba(90,63,216,.4))"></div>
  <div class="abs" style="left:17px;top:58px;display:flex;align-items:center;gap:4px">
    <span style="width:11px;height:11px;border-radius:50%;background:#fff"></span>
    <span style="font-size:9px;font-weight:700;color:#fff;line-height:1">VELORA SYSTEMS<br>GROUP</span>
  </div>
  <div class="abs" style="left:17px;top:105px;font-size:8.5px;font-weight:700;color:#fff">CONTACT US</div>
  <div class="abs" style="left:17px;top:118px;font-size:5px;line-height:7.8px;color:#fff">
    <div>&#9742; 555-014-288</div>
    <div>&#9993; hello@velorasystemsgroup.com</div>
    <div>&#9679; Your address, your city, box 88900</div>
    <div>www.velorasystemsgroup.com</div>
  </div>
</section>

</main>
</body>
</html>
```